Gorvane Rum Liqueur Bottle Label

I will be launching a Rum Liqueur called Gorvane Spiced Rum Liqueur. The bottle I have chosen to use is an TKV 500ml type and I have included a photo of it in the project brief. The bottle dimensions are height 193.5mm with diameter 85mm. There will be a cork closure, sealed with a heat shrink capsule. I require two labels for each bottle, a large rectangular label on the front with the product name, logo, label design and the bottle quantity which is 500ml. The front label should also contain the strength of the liqueur which is 25% vol. The rear label will contain the required UK legal information such as government health warning, number of UK units of alcohol as well as the place of bottling which is Wick, Caithness, Scotland. A barcode will also be on the rear label and I have added it as a jpg file. On my current homemade label I also have the following text on the rear label: "Due to the ferocious tides, currents and winds that shape the narrow stretch of water separating Caithness from the Orkney Islands in the far North of Scotland, it has become known to generations of sailors as "Gorvane" and is the graveyard of countless number of ships. Gorvane Spiced Rum Liqueur aims to capture the spirit of those brave men and women who have risked all on these treacherous shores". For the main front label I am keen for the designer to explore the themes of shipwreck, sea monsters, smuggling, pistols, diving helmets, heavy seas, sea stacks, high cliffs, sealife etc. I have included a story about a local smuggler called Peter Lurrick as an example of an inspirational theme. I currently also have a website regarding Caithness shipwrecks which can be found at www.gorvane-example.com and which could provide some further ideas. My feeling is that the label design should be masculine and I would like to keep away from designs that would make the label costly to print. I have included a file with my current logo but please feel free to change its colour as required and to remove the word Gorvane from the logo if you wish. I can supply the logo file in different formats such as jpg, ai, eps, pdf, png or psd. I also have the barcode in pdf, png or svg formats. The word Gorvane is a registered trademark.I have also attached a photograph of my liqueur in an attempt to show the colour of the finished product and the bottle style.
Colors
Designer to choose colors to be used in the design.
Look and feel
Each slider illustrates characteristics of the customer's brand and the style your logo design should communicate.

```html
<!DOCTYPE html>
<html lang="en">
<head>
<meta charset="utf-8">
<title>Gorvane Spiced Rum Liqueur – Front Label</title>
<link href="https://fonts.googleapis.com/css2?family=Rye&family=Oswald:wght@400;500&display=swap" rel="stylesheet">
<style>
  :root {
    --backdrop: #ecebe8;
    --label-ground: #2b2420;
    --gold: #c9b878;
    --gold-dark: #8f7f47;
    --cream: #efe8d4;
    --art-tone: #6b625a;
    --art-light: #b9b3ab;
  }
  html, body {
    margin: 0;
    padding: 0;
    width: 806px;
    height: 1200px;
    overflow: hidden;
    background: var(--backdrop);
  }
  .canvas {
    position: relative;
    width: 806px;
    height: 1200px;
  }
  .front-label {
    position: absolute;
    left: 83px;
    top: 240px;
    width: 640px;
    height: 720px;
  }
  .label-frame {
    position: absolute;
    inset: 0;
    width: 640px;
    height: 720px;
  }
  .label-artwork {
    position: absolute;
    left: 150px;
    top: 90px;
    width: 340px;
    height: 300px;
    border-radius: 6px;
    background: radial-gradient(ellipse at 50% 45%, var(--art-light) 0%, var(--art-tone) 55%, var(--label-ground) 100%);
  }
  .name-band {
    position: absolute;
    left: 95px;
    top: 405px;
    width: 450px;
    height: 82px;
    box-sizing: border-box;
    border: 3px solid var(--cream);
    background: var(--label-ground);
    display: flex;
    align-items: center;
    justify-content: center;
    transform: rotate(2deg);
  }
  .product-name {
    margin: 0;
    font-family: "Rye", serif;
    font-weight: 400;
    font-size: 58px;
    letter-spacing: 2px;
    color: var(--cream);
    line-height: 1;
  }
  .style-band {
    position: absolute;
    left: 130px;
    top: 505px;
    width: 400px;
    height: 56px;
    box-sizing: border-box;
    border: 3px solid var(--gold);
    background: var(--label-ground);
    display: flex;
    align-items: center;
    justify-content: center;
    transform: rotate(4deg);
  }
  .product-style {
    margin: 0;
    font-family: "Oswald", sans-serif;
    font-weight: 500;
    font-size: 32px;
    letter-spacing: 1px;
    text-transform: uppercase;
    color: var(--cream);
    line-height: 1;
  }
  .strength {
    position: absolute;
    left: 0;
    right: 0;
    top: 600px;
    margin: 0;
    text-align: center;
    font-family: "Oswald", sans-serif;
    font-weight: 400;
    font-size: 30px;
    color: var(--gold);
  }
</style>
</head>
<body>
<div class="canvas">
  <section class="front-label">
    <svg class="label-frame" viewBox="0 0 640 720" aria-hidden="true">
      <path fill="var(--label-ground)" stroke="var(--gold)" stroke-width="5"
        d="M320 20 Q380 40 460 55 L560 95 L620 95 L620 290 Q590 300 590 360 Q590 420 620 430 L620 625 L560 625 L460 665 Q380 680 320 700 Q260 680 180 665 L80 625 L20 625 L20 430 Q50 420 50 360 Q50 300 20 290 L20 95 L80 95 L180 55 Q260 40 320 20 Z"/>
      <path fill="none" stroke="var(--gold-dark)" stroke-width="2"
        d="M320 38 Q376 56 452 70 L552 110 L604 110 L604 280 Q574 296 574 360 Q574 424 604 440 L604 610 L552 610 L452 650 Q376 664 320 682 Q264 664 188 650 L88 610 L36 610 L36 440 Q66 424 66 360 Q66 296 36 280 L36 110 L88 110 L188 70 Q264 56 320 38 Z"/>
    </svg>
    <div class="label-artwork" role="img" aria-label="Engraved illustration of a brass diving helmet behind a rum barrel with an anchor, rope and a seagull"></div>
    <div class="name-band">
      <h1 class="product-name">GORVANE</h1>
    </div>
    <div class="style-band">
      <p class="product-style">Spiced Rum Liqueur</p>
    </div>
    <p class="strength">25% vol.</p>
  </section>
</div>
</body>
</html>
```